Makeup Artist Requires Business Card design

Hi

I am looking for a business card design to market my makeup artist business. I operate under my own name Mara Veldt and I would like to keep the design of the card very simplistic and chic - something that keeps both my name and profession (makeup artist) the focus of the card. I would like it to be a style that is eyecatching to the reader (i am open to anything unusual) but upmarket.

Target Market(s)

women, magazine/beauty/fashion editors, photographers.

Industry/Entity Type

Business

Requirements
Must have
• Must contain:

Phone number: 0418 372 915
Website: www.maraveldt.com.au
email: contact@maraveldt.com.au

(although you don't need to have prefaced these with the words phone number, website etc :))
Should not have
• I am not looking for anything overly colorful - my preference is to keep the card dark if possible.

```html
<!DOCTYPE html>
<html lang="en">
<head>
<meta charset="utf-8">
<title>Mara Veldt – Makeup Artist Business Card</title>
<link rel="stylesheet" href="https://fonts.googleapis.com/css2?family=Source+Sans+3:wght@300;400;600&display=swap">
<style>
  :root {
    --card-black: #070707;
    --ornament-dark: #161616;
    --ornament-mid: #2e2e2e;
    --ornament-light: #4a4a4a;
    --text-white: #ffffff;
    --label-taupe: #8c847c;
  }
  html, body {
    margin: 0;
    padding: 0;
    width: 1200px;
    height: 720px;
    overflow: hidden;
    background: var(--card-black);
  }
  .business-card {
    position: relative;
    width: 1200px;
    height: 720px;
    overflow: hidden;
    font-family: "Source Sans 3", "Myriad Pro", Arial, sans-serif;
    color: var(--text-white);
  }
  .damask-backdrop {
    position: absolute;
    inset: 0;
    background:
      radial-gradient(ellipse 70% 90% at 85% 55%, var(--ornament-light) 0%, var(--ornament-mid) 45%, transparent 80%),
      linear-gradient(100deg, var(--card-black) 0%, var(--ornament-dark) 30%, var(--ornament-mid) 70%, var(--ornament-dark) 100%);
  }
  .identity {
    position: absolute;
    left: 121px;
    top: 132px;
  }
  .identity__name {
    margin: 0;
    font-weight: 600;
    font-size: 86px;
    line-height: 1;
    letter-spacing: -0.045em;
  }
  .identity__role {
    margin: 8px 0 0 6px;
    font-weight: 300;
    font-size: 33px;
    line-height: 1;
    letter-spacing: 0.1em;
  }
  .contact {
    position: absolute;
    left: 132px;
    top: 462px;
    margin: 0;
    font-size: 25px;
    line-height: 32px;
    letter-spacing: 0.01em;
  }
  .contact__row {
    display: flex;
  }
  .contact__label {
    color: var(--label-taupe);
    width: 87px;
  }
  .contact__value {
    color: var(--text-white);
  }
  .contact__row--web {
    margin-top: 30px;
  }
  .contact__row--web .contact__label {
    width: auto;
    margin-right: 6px;
  }
</style>
</head>
<body>
  <main class="business-card">
    <div class="damask-backdrop" role="img" aria-label="Dark grey damask pattern of swirling leaves and scrolls, brightening toward the right"></div>

    <header class="identity">
      <h1 class="identity__name">Mara Veldt</h1>
      <p class="identity__role">makeup artist</p>
    </header>

    <address class="contact">
      <div class="contact__row"><span class="contact__label">Tel:</span><span class="contact__value">0418 372 915</span></div>
      <div class="contact__row"><span class="contact__label">Email:</span><span class="contact__value">contact@maraveldt.com.au</span></div>
      <div class="contact__row contact__row--web"><span class="contact__label">Website:</span><span class="contact__value">www.maraveldt.com.au</span></div>
    </address>
  </main>
</body>
</html>
```